Brackwell Immigration Law

We need a web design for our existing company www.brackwellcounsel.co.uk. We are an immigration consultancy. The final design should communicate professionalism, integrity and affordability.

Industry/Entity Type

It Company

Logo Text

Brackwell Counsel Partners

Number of Pages Required

5+ page

Font styles to use
Serif

Requirements
Must have
• I want to have the same silhouette logo but something different in positioning..
Nice to have
• Please have a look at these websites:
• https://www.travelpathguide.co.uk/visa_uk/
• http://www.oakdenadvisers.co.uk/
• http://www.myrtlegatelaw.org/index.php
• www.brackwellcounsel.co.uk

```html
<!DOCTYPE html>
<html lang="en">
<head>
<meta charset="utf-8">
<title>Brackwell Counsel Partners</title>
<link href="https://fonts.googleapis.com/css2?family=Arimo:wght@400;700&display=swap" rel="stylesheet">
<style>
:root{
  --accent:#b5433f;
  --guide:#efc8c6;
  --ink:#2e2e2e;
  --muted:#666;
  --panel:#f1f1f1;
  --footer:#2a2a2a;
  --white:#fff;
}
*{box-sizing:border-box;margin:0;padding:0}
html,body{width:1200px;height:2648px;overflow:hidden}
body{position:relative;background:var(--white);font-family:"Arimo",Arial,sans-serif;color:var(--ink)}
.guide-v{position:absolute;top:0;bottom:108px;width:1px;background:var(--guide)}
.guide-h{position:absolute;left:0;right:0;height:1px;background:var(--guide)}
.main-nav{position:absolute;top:0;left:0;right:0;height:40px;display:flex;justify-content:space-around;padding:0 90px;align-items:center;font-size:12px;letter-spacing:.5px}
.main-nav a{color:var(--ink);text-decoration:none}
.main-nav a.active{color:var(--accent)}
.brand{position:absolute;top:120px;left:0;right:0;display:flex;justify-content:center;align-items:center;gap:12px}
.brand-mark{width:26px;height:26px;background:var(--ink)}
.brand-name{font-size:20px;font-weight:700;color:var(--ink)}
.hero{position:absolute;top:240px;left:0;right:0;height:480px;background:linear-gradient(120deg,#e9ecef 0%,#b9bec4 30%,#f4f5f6 50%,#8f959c 70%,#dfe2e5 100%)}
.hero-box{position:absolute;left:100px;top:105px;width:1000px;height:295px;background:rgba(255,255,255,.72);text-align:center}
.hero-box h1{margin-top:45px;font-size:40px;font-weight:700}
.hero-box p{margin-top:18px;font-size:28px}
.btn{display:inline-block;background:var(--accent);color:var(--white);font-size:12px;letter-spacing:.5px;padding:13px 26px;text-decoration:none}
.hero-box .btn{margin-top:52px}
.hero-dot{position:absolute;left:596px;top:443px;width:8px;height:8px;border-radius:50%;background:var(--accent)}
h2{font-size:40px;font-weight:700}
.col{position:absolute;width:490px;font-size:21px;line-height:28px}
.col p{margin-top:22px}
.rule-btn{position:absolute;left:600px;width:540px;height:3px;background:var(--accent)}
.rule-btn .btn{position:absolute;right:50px;bottom:0;width:155px;text-align:center}
.team-head{position:absolute;left:90px;top:1150px}
.team-head h3{font-size:30px;margin-top:4px}
.member{position:absolute;top:1330px;width:260px;text-align:center}
.photo{width:240px;height:240px;border-radius:50%;margin:0 auto;background:radial-gradient(circle at 50% 40%,#d8d8d8,#8a8a8a)}
.member h4{font-size:24px;margin-top:16px}
.member p{font-size:13px;color:var(--muted);line-height:16px;margin:6px 30px 0}
.press{position:absolute;left:60px;top:1730px;width:540px;height:810px;background:var(--panel);padding:45px 30px}
.press .lead{font-size:30px;line-height:34px;margin-top:6px}
.press .body{font-size:13px;line-height:17px;margin-top:30px}
.more-link{display:block;text-align:right;font-size:11px;color:var(--muted);margin-top:36px;text-decoration:none}
.news{margin-top:10px}
.news h2{font-size:36px}
.news-item{margin-top:24px;color:var(--muted);font-size:15px;line-height:19px}
.news-item time{display:block;font-size:10px;margin-top:3px}
.contact{position:absolute;left:625px;top:1775px;width:465px}
.contact .intro{font-size:14px;line-height:17px;margin-top:4px}
.contact form{margin-top:50px}
.field{display:block;width:100%;height:30px;border:1px solid var(--accent);margin-bottom:15px;font-size:12px;color:var(--muted);padding:7px 8px;background:var(--white)}
.field.textarea{height:130px}
.send{display:block;margin-left:auto;background:var(--accent);color:var(--white);font-size:14px;border:0;width:50px;height:34px;font-family:inherit}
.site-footer{position:absolute;left:0;right:0;bottom:0;height:108px;background:var(--footer);color:#ddd}
.site-footer small{position:absolute;left:90px;top:48px;font-size:13px}
.social{position:absolute;right:90px;top:42px;display:flex;gap:26px}
.social span{width:18px;height:18px;border-radius:50%;background:#ddd}
</style>
</head>
<body>
<div class="guide-v" style="left:60px"></div>
<div class="guide-v" style="left:1140px"></div>
<div class="guide-h" style="top:40px"></div>
<div class="guide-h" style="top:1090px;background:var(--accent);opacity:.5"></div>
<div class="guide-h" style="top:1730px;background:var(--accent);opacity:.5"></div>

<nav class="main-nav">
  <a class="active" href="#">HOME</a><a href="#">ABOUT US</a><a href="#">JOIN US</a><a href="#">BLOG</a><a href="#">CONTACT</a>
</nav>

<div class="brand"><span class="brand-mark"></span><span class="brand-name">Brackwell Counsel Partners</span></div>

<section class="hero" role="img" aria-label="Grey photo of modern glass office architecture">
  <div class="hero-box">
    <h1>Legal services</h1>
    <p>Lorem Ipsum is simply dummy text of the printing and typesetting industry.</p>
    <a class="btn" href="#">LEARN MORE</a>
  </div>
  <span class="hero-dot"></span>
</section>

<section class="col" style="left:90px;top:765px">
  <h2>Practic</h2>
  <p>Lorem Ipsum is simply dummy text of the printing and typesetting industry. Lorem Ipsum has been the industry's standard dummy text ever since the 1500s, when an unknown printer took a galley of type and scrambled it to make a type specimen book. It has survived not only five centuries, but also the leap into electronic typesetting</p>
</section>
<section class="col" style="left:625px;top:765px">
  <h2>Scope of work</h2>
  <p>Lorem Ipsum is simply dummy text of the printing and typesetting industry. Lorem Ipsum has been the industry's standard dummy text ever since the 1500s, when an unknown printer took a galley of type and scrambled it to make a type specimen book. It has</p>
</section>
<div class="rule-btn" style="top:1084px"><a class="btn" href="#">LEARN MORE</a></div>

<div class="team-head"><h2>Our Team</h2><h3>70 lawyers</h3></div>
<div class="member" style="left:120px"><div class="photo" role="img" aria-label="Portrait photo of lawyer James Okoro"></div><h4>James Okoro</h4><p>Lorem Ipsum is simply dummy text of the printing and typesetting industry.</p></div>
<div class="member" style="left:480px"><div class="photo" role="img" aria-label="Portrait photo of lawyer Tessa Rowan"></div><h4>Tessa Rowan</h4><p>Lorem Ipsum is simply dummy text of the printing and typesetting industry.</p></div>
<div class="member" style="left:840px"><div class="photo" role="img" aria-label="Portrait photo of lawyer Kevin Lam"></div><h4>Kevin Lam</h4><p>Lorem Ipsum is simply dummy text of the printing and typesetting industry.</p></div>
<div class="rule-btn" style="top:1727px"><a class="btn" href="#">LEARN MORE</a></div>

<section class="press">
  <h2>Press</h2>
  <p class="lead">Lorem Ipsum is simply dummy text of the printing and typesetting industry.</p>
  <p class="body">Lorem Ipsum is simply dummy text of the printing and typesetting industry. Lorem Ipsum has been the industry's standard dummy text ever since the 1500s.Lorem Ipsum is simply dummy text of the printing and typesetting industry. Lorem Ipsum has been the industry's standard dummy text ever since the 1500s.Lorem Ipsum is simply dummy text of the printing and typesetting industry.</p>
  <a class="more-link" href="#">LEARN MORE</a>
  <div class="news">
    <h2>News</h2>
    <div class="news-item">New bills amending the current immigration rules...<time>05.03.2023</time></div>
    <div class="news-item">Wider access to the global network and visa services<time>12.03.2023</time></div>
    <div class="news-item">Unprecedented events in legal practice in 2023<time>21.03.2023</time></div>
  </div>
</section>

<section class="contact">
  <h2>Contact Us</h2>
  <p class="intro">Lorem Ipsum is simply dummy text of the printing and typesetting industry. Lorem Ipsum has been the industry's standard dummy text ever since the 1500s.</p>
  <form>
    <span class="field">Name</span>
    <span class="field">Email</span>
    <span class="field">Theme</span>
    <span class="field textarea">Text</span>
    <button class="send" type="button">Send</button>
  </form>
</section>

<footer class="site-footer">
  <small>© 2023 «Brackwell»</small>
  <div class="social"><span></span><span></span><span></span><span></span></div>
</footer>
</body>
</html>
```